Verpackungsdesign für einen Glückskeks
Zielgruppe
Wir sind ein kleines junges Unternehmen, dass sich auf die regionale Herstellung von hochwertigen Glückskeksen und Fruchtgummis als Gastgeschenke für diverse Feierlichkeiten spezialisiert hat. Unter Anderem unsere 'Wie fein, mit euch hier' Glückskekse sind ein Bestseller.
Aufgabenstellung
Ich habe beim Design noch keine Vorstellungen und freue mich auf diverse Vorschläge.
Das Design kann im Querformat oder Hochformat sein.
Ich benötige ein Verpackungsdesign für einen Glückskeks. Es handelt sich um eine Plastikfolie in den Maßen 11x7cm.
Thema: Fußball
Primär soll das Design allgemein zum Thema Fußball für Geburtstage, Feiern, Public Viewing, etc. passen. Sekundär soll das Design die kommende Europameisterschaft aufgreifen aber nicht einzig darauf limitiert sein. Auch soll das Design sprachlich für diverse Märkte in Europa abgewandelt werden können.
Das Design soll hohe Qualität ausstrahlen.
Anbei ein Beispielfoto eines unserer fertigen Produkte, um die Verpackung zu zeigen.
Außerdem auch eine Standzeichnung der gesamten Verpackungsfolie.

```html
<!DOCTYPE html>
<html lang="de">
<head>
<meta charset="utf-8">
<title>Glückskeks Verpackung – Fußball</title>
<link rel="stylesheet" href="https://fonts.googleapis.com/css2?family=Barlow+Condensed:wght@700&display=swap">
<style>
  :root {
    --stage: #b4b4b6;
    --navy-deep: #0a0d5e;
    --navy: #14169a;
    --violet: #8a2be2;
    --cyan: #27d9f0;
    --ink-light: #ffffff;
  }
  html, body {
    margin: 0;
    padding: 0;
    width: 1084px;
    height: 1200px;
    overflow: hidden;
    background: var(--stage);
  }
  .stage {
    position: relative;
    width: 1084px;
    height: 1200px;
  }
  .wrapper-design {
    position: absolute;
    left: 92px;
    top: 313px;
    width: 900px;
    height: 573px;
    overflow: hidden;
    background: var(--navy-deep);
    box-shadow: 0 6px 18px rgba(0,0,0,0.25);
  }
  .wrapper-design svg.backdrop {
    position: absolute;
    inset: 0;
  }
  .star-ball-decoration {
    position: absolute;
    left: -60px;
    top: 40px;
    width: 470px;
    height: 500px;
    border-radius: 50%;
    background: radial-gradient(circle at 40% 55%, rgba(39,217,240,0.55), rgba(138,43,226,0.35) 55%, rgba(20,22,154,0) 75%);
  }
  .player-silhouette {
    position: absolute;
    left: 596px;
    top: 72px;
    width: 290px;
    height: 410px;
    border-radius: 140px 140px 60px 60px;
    background: linear-gradient(160deg, var(--violet) 0%, #4f7cf0 45%, var(--cyan) 75%, #5a8cf0 100%);
    opacity: 0.85;
  }
  .football {
    position: absolute;
    left: 658px;
    top: 326px;
    width: 60px;
    height: 60px;
    border-radius: 50%;
    background: radial-gradient(circle at 40% 40%, #5a6ef0, #1b1f9a);
  }
  .slogan {
    position: absolute;
    left: 150px;
    top: 150px;
    width: 520px;
    margin: 0;
    font-family: 'Barlow Condensed', 'Arial Narrow', sans-serif;
    font-weight: 700;
    color: var(--ink-light);
    text-align: center;
    line-height: 0.86;
    letter-spacing: 1px;
    transform: rotate(-6deg);
    transform-origin: center;
    text-shadow: 0 2px 6px rgba(0,0,40,0.35);
  }
  .slogan span { display: block; }
  .slogan .line-top { font-size: 118px; }
  .slogan .line-mid { font-size: 130px; }
  .slogan .line-bottom { font-size: 84px; padding-left: 120px; }
</style>
</head>
<body>
<main class="stage">
  <section class="wrapper-design">
    <svg class="backdrop" width="900" height="573" viewBox="0 0 900 573" aria-hidden="true">
      <defs>
        <linearGradient id="base" x1="0" y1="0" x2="1" y2="0">
          <stop offset="0" stop-color="#1a2bb0"/>
          <stop offset="0.5" stop-color="#141690"/>
          <stop offset="1" stop-color="#0a0d5e"/>
        </linearGradient>
        <radialGradient id="glowCyan" cx="0.5" cy="0.5" r="0.5">
          <stop offset="0" stop-color="#27d9f0" stop-opacity="0.9"/>
          <stop offset="1" stop-color="#27d9f0" stop-opacity="0"/>
        </radialGradient>
        <radialGradient id="glowViolet" cx="0.5" cy="0.5" r="0.5">
          <stop offset="0" stop-color="#a23cf0" stop-opacity="0.8"/>
          <stop offset="1" stop-color="#a23cf0" stop-opacity="0"/>
        </radialGradient>
      </defs>
      <rect width="900" height="573" fill="url(#base)"/>
      <ellipse cx="60" cy="480" rx="200" ry="160" fill="url(#glowCyan)"/>
      <ellipse cx="330" cy="420" rx="90" ry="200" fill="url(#glowViolet)"/>
      <ellipse cx="260" cy="40" rx="220" ry="90" fill="url(#glowViolet)" opacity="0.7"/>
      <ellipse cx="150" cy="180" rx="130" ry="110" fill="url(#glowCyan)" opacity="0.6"/>
    </svg>
    <div class="star-ball-decoration" role="img" aria-label="Glühende Sternen-Fußball-Grafik als Hintergrunddekoration"></div>
    <div class="player-silhouette" role="img" aria-label="Silhouette eines Fußballspielers beim Schuss, Farbverlauf violett bis türkis"></div>
    <div class="football" role="img" aria-label="Kleiner Fußball"></div>
    <h1 class="slogan">
      <span class="line-top">SIEGE</span>
      <span class="line-mid">BEGINNEN</span>
      <span class="line-bottom">IM HERZEN</span>
    </h1>
  </section>
</main>
</body>
</html>
```